Quillfield HVAC WordPress website design

Design a new modern, clean, website for HVAC mechanical business that uses company logo/colors for branding and recognition. Files attached are just for band and color information. Here is a website design that appeals to me https://www.kestwellpartners.com/

A clear description of who we are and what we do

An easily-navigated site map

An easily-navigated site map for mobile devices

Easy-to-find contact information

Obvious call to action for service, installs or to schedule estimates

about us page

Provide a way for potential customers to contact us via text or email

provide a way that allows a customer to upload a picture to request a service call or quote.

I'm looking for the design to be completed in WordPress

Industry/Entity Type

HVAC Mechanical & Building Automation / Controls contractor

Coding

Coded - Design and coding required

Number of Pages Required

5+ page

Colors
0054AA
0677BA
7BADD7
CADEEF
E8F1F8

Requirements
Must have
• Design a new modern, clean, website for HVAC mechanical business that uses company logo/colors for branding and recognition. Files attached are just for band and color information. Here is a website design that appeals to me https://www.kestwellpartners.com/ A clear description of who we are and what we do An easily-navigated site map An easily-navigated site map for mobile devices Easy-to-find contact information Obvious call to action for service, installs or to schedule estimates about us page Provide a way for potential customers to contact us via text or email provide a way that allows a customer to upload a picture to request a service call or quote.
Nice to have

```html
<!DOCTYPE html>
<html lang="en">
<head>
<meta charset="utf-8">
<title>Quillfield HVAC – Heating &amp; Air Conditioning Service</title>
<link href="https://fonts.googleapis.com/css2?family=Roboto:wght@300;400;500;700&family=Tinos:wght@700&display=swap" rel="stylesheet">
<style>
:root{
  --brand:#0054AA;
  --brand-2:#0677BA;
  --sky:#7BADD7;
  --mist:#CADEEF;
  --ice:#E8F1F8;
  --navy:#0B2352;
  --ink:#222831;
  --muted:#6b7380;
  --white:#ffffff;
  --star:#f2b01e;
}
*{box-sizing:border-box;margin:0;padding:0}
html,body{width:1200px;height:4542px;overflow:hidden}
body{position:relative;font-family:'Roboto',sans-serif;color:var(--ink);background:var(--white)}
.abs{position:absolute}
a{color:inherit;text-decoration:none}

/* Hero */
.hero{left:0;top:0;width:1200px;height:740px;overflow:hidden}
.hero-bg{position:absolute;inset:0;background:linear-gradient(135deg,#0a2a6b 0%,#164a95 40%,#2b5d9f 65%,#2d5f6a 100%)}
.brand{display:flex;align-items:center;gap:12px;font-weight:700;color:var(--white);font-size:30px;letter-spacing:.5px}
.brand .mark{width:34px;height:34px;border-radius:50%;background:var(--white)}
.topbar-phone{left:770px;top:28px;display:flex;align-items:center;gap:12px;color:var(--white);font-size:17px}
.topbar-phone .ic{width:30px;height:30px;border-radius:50%;background:var(--white);display:flex;align-items:center;justify-content:center}
.btn-quote{left:975px;top:21px;width:155px;height:42px;background:var(--brand);color:var(--white);font-size:16px;display:flex;align-items:center;justify-content:center}
.nav-line{left:335px;top:80px;width:795px;height:1px;background:rgba(255,255,255,.35)}
.nav{top:97px;left:0;width:1200px;color:var(--white);font-size:17px;font-weight:500}
.nav a{position:absolute;top:0}
.nav .active::after{content:"";position:absolute;left:0;right:0;bottom:-8px;height:2px;background:var(--white)}
.hero-title{right:536px;top:240px;text-align:right;font-family:'Tinos',serif;font-weight:700;color:var(--white);font-size:38px;line-height:48px;text-transform:uppercase}
.hero-title .dash{display:inline-block;width:56px;height:3px;background:var(--sky);vertical-align:middle;margin-right:18px}
.hero-sub{right:536px;top:348px;color:var(--white);font-size:22px;font-weight:300}
.van-art{left:0;top:410px;width:580px;height:300px;border-radius:0 140px 0 0;background:linear-gradient(180deg,#eef2f6,#c6ced8)}
.hero-wave{left:0;top:640px;width:1200px;height:110px}

.book{left:754px;top:203px;width:331px;height:428px;background:var(--brand);border-radius:10px;padding:36px 28px 0 36px;color:var(--white);box-shadow:0 10px 30px rgba(0,0,0,.25)}
.book h2{font-size:26px;font-weight:500}
.book p{font-size:13px;line-height:19px;margin-top:8px;opacity:.9;width:240px}
.field{position:absolute;left:28px;width:275px;height:39px;background:var(--ice);border-radius:3px;color:#8a95a5;font-size:13px;padding:0 16px;display:flex;align-items:center;justify-content:space-between}
.book .submit{position:absolute;left:28px;top:343px;width:275px;height:44px;background:var(--sky);color:var(--white);font-size:17px;display:flex;align-items:center;justify-content:center;border-radius:3px}

/* Section headings */
.h-center{left:0;width:1200px;text-align:center}
.underline{height:3px;background:var(--brand)}
.what-title{top:808px;font-size:58px;font-weight:300}
.what-title b{font-weight:700}

.svc{width:282px;height:313px;background:var(--white);border-radius:140px 140px 6px 6px;box-shadow:0 8px 28px rgba(20,60,120,.09);text-align:center;padding-top:40px}
.svc h3{font-size:21px;font-weight:500;margin-top:16px}
.svc .bar{width:36px;height:2px;background:var(--brand);margin:18px auto 0}
.svc p{font-size:14px;line-height:24px;color:var(--muted);margin-top:12px}
.dot{width:20px;height:20px;border-radius:50%;background:var(--brand-2)}
.pill{background:var(--brand);color:var(--white);border-radius:28px;font-size:17px;display:flex;align-items:center;justify-content:center}

/* Treat */
.treat-bg{left:0;top:1440px;width:1200px;height:701px}
.art{display:block}
.treat-title{left:638px;top:1628px;font-size:33px;font-weight:300;color:var(--ink);display:flex;align-items:center;gap:16px}
.treat-title b{color:var(--brand);font-weight:700}
.treat-title .ln{width:50px;height:3px;background:var(--brand)}
.treat-copy{left:638px;top:1680px;width:440px;font-size:14px;line-height:26px;color:#4d5663}
.treat-list{font-size:16px;font-weight:500;line-height:30px;list-style:none}
.treat-list li{display:flex;align-items:center;gap:10px}
.treat-list li::before{content:"";width:11px;height:11px;border:1.5px solid var(--brand);border-radius:50%}

/* Testimonials */
.cl-title{left:111px;top:2210px;font-size:35px;font-weight:300}
.cl-title b{color:var(--brand);font-weight:700}
.review{top:2317px;width:308px;height:211px;background:#eef1f5;border-radius:6px;padding:60px 33px 0;font-size:13px;line-height:21px;color:#7b828c}
.review.featured{background:var(--brand);color:var(--white);box-shadow:0 10px 22px rgba(0,84,170,.35)}
.review .who{position:absolute;left:33px;top:160px;font-size:13px;line-height:18px;color:var(--ink)}
.review.featured .who{color:var(--white)}
.review .who small{display:block;font-size:12px}
.review .stars{position:absolute;right:38px;top:162px;color:var(--star);font-size:15px;letter-spacing:3px}
.review .stars i{color:#c5c9cf;font-style:normal}
.avatar{position:absolute;top:-40px;width:78px;height:78px;border-radius:50%;background:linear-gradient(160deg,#c9ced6,#8d96a3);border:3px solid var(--white)}

/* CTA */
.cta-bg{left:0;top:2661px;width:1200px;height:560px}
.cta-title{left:111px;top:2722px;color:var(--white);font-size:46px;font-weight:700;line-height:57px}
.cta-sub{left:111px;top:2920px;color:var(--white);font-size:26px;font-weight:500}
.cta-copy{left:111px;top:2976px;width:520px;color:#d5e3f3;font-size:14px;line-height:27px}
.btn-white{background:var(--white);color:var(--brand);font-size:17px;display:flex;align-items:center;justify-content:center}
.btn-line{border:1.5px solid var(--white);color:var(--white);font-size:17px;display:flex;align-items:center;justify-content:center}
.van-photo{left:670px;top:2722px;width:426px;height:441px;border-radius:60px 60px 30px 30px;background:linear-gradient(180deg,#1f4f9c,#f1f3f6 45%,#cfd5dd 80%,#2a2f38)}

/* About */
.about-title{top:3306px;font-size:38px;font-weight:300}
.about-title b{color:var(--brand);font-weight:700}
.about-lead{top:3370px;font-size:20px;color:#2c323b}
.about-copy{left:210px;top:3423px;width:780px;text-align:center;font-size:16px;line-height:31px;color:#5a626d}
.banner{left:113px;top:3681px;width:976px;height:250px;background:linear-gradient(90deg,#1c3f7a 0%,#3a5f94 55%,#8ea4bf 100%)}
.banner-text{left:166px;top:3776px;color:var(--white);font-size:36px;font-weight:700;line-height:44px}
.btn-blue{background:var(--brand);color:var(--white);font-size:17px;display:flex;align-items:center;justify-content:center}

/* Footer */
.footer{left:0;top:3970px;width:1200px;height:572px;background:var(--navy);color:var(--white)}
.f-quality{left:738px;top:4058px;font-size:29px;line-height:44px;font-weight:400;text-transform:uppercase;color:var(--white)}
.f-head{font-size:18px;font-weight:700;text-transform:uppercase;color:var(--white)}
.f-ic{width:52px;height:52px;border-radius:10px;background:var(--brand);display:flex;align-items:center;justify-content:center}
.f-text{font-size:16px;line-height:22px;color:var(--white)}
.f-text span{color:#aeb9cc;display:block}
.f-links{list-style:none;font-size:15px;line-height:27.5px;color:#aeb9cc}
.f-links li{display:flex;align-items:center;gap:12px}
.f-links li::before{content:"";width:13px;height:13px;border-radius:50%;background:#7f8ca5}
.f-input{left:740px;top:4216px;width:349px;height:49px;border-radius:25px;background:#1d3f7d;color:#9bb0d2;font-size:15px;display:flex;align-items:center;padding-left:32px}
.f-submit{left:740px;top:4282px;width:152px;height:46px;border-radius:23px;background:var(--brand);color:var(--white);display:flex;align-items:center;padding-left:26px;gap:18px;font-size:16px}
.f-submit .ar{width:34px;height:34px;border-radius:50%;background:var(--sky);display:flex;align-items:center;justify-content:center}
.f-rule{left:111px;top:4454px;width:978px;height:1px;background:#33507f}
.f-bottom{top:4486px;font-size:14px;color:#aeb9cc}
.social{top:4482px;width:30px;height:30px;border-radius:50%;background:var(--white)}
</style>
</head>
<body>

<!-- HERO -->
<section class="abs hero">
  <div class="hero-bg" role="img" aria-label="Photo of a modern glass office building under a blue sky"></div>
  <div class="abs" style="left:70px;top:62px"><div class="brand"><span class="mark"></span>Quillfield HVAC</div></div>
  <div class="abs topbar-phone"><span class="ic"><svg width="16" height="16" viewBox="0 0 24 24"><path d="M6.6 10.8a15 15 0 006.6 6.6l2.2-2.2a1 1 0 011-.25 11.4 11.4 0 003.6.57 1 1 0 011 1V20a1 1 0 01-1 1A17 17 0 013 4a1 1 0 011-1h3.5a1 1 0 011 1c0 1.25.2 2.45.57 3.57a1 1 0 01-.25 1z" fill="#0054AA"/></svg></span>555 014 2290</div>
  <a class="abs btn-quote" href="#">Get A Quote</a>
  <div class="abs nav-line"></div>
  <nav class="abs nav">
    <a class="active" style="left:557px" href="#">Home</a>
    <a style="left:664px" href="#">Our Services</a>
    <a style="left:830px" href="#">About Us</a>
    <a style="left:966px" href="#">Blog</a>
    <a style="left:1062px" href="#">Contact</a>
  </nav>
  <h1 class="abs hero-title"><span class="dash"></span>Heating &amp; Air<br>Conditioning Service</h1>
  <p class="abs hero-sub">Bringing You More Than Just Air</p>
  <div class="abs van-art" role="img" aria-label="Illustration of the white company service van"></div>
  <svg class="abs hero-wave" viewBox="0 0 1200 110" preserveAspectRatio="none">
    <path d="M0 70 C300 75 700 75 1200 0 L1200 110 L0 110Z" fill="#ffffff"/>
    <path d="M0 70 C300 75 700 75 1200 0 L1200 12 C700 82 300 86 0 82Z" fill="#0054AA"/>
  </svg>
  <form class="abs book">
    <h2>Book Our Service</h2>
    <p>We make sure your air conditioning and heating systems.</p>
    <div class="field" style="top:137px">Name</div>
    <div class="field" style="top:188px">Phone</div>
    <div class="field" style="top:238px">Email Address</div>
    <div class="field" style="top:289px">Choose Services <svg width="12" height="8" viewBox="0 0 12 8"><path d="M1 1l5 5 5-5" stroke="#6b7380" stroke-width="1.5" fill="none"/></svg></div>
    <div class="submit">SUBMIT</div>
  </form>
</section>

<!-- WHAT WE DO -->
<h2 class="abs h-center what-title">What <b>We Do</b></h2>
<div class="abs underline" style="left:563px;top:890px;width:74px"></div>

<div class="abs dot" style="left:240px;top:923px"></div>
<div class="abs dot" style="left:938px;top:920px"></div>
<div class="abs dot" style="left:589px;top:1246px"></div>

<article class="abs svc" style="left:109px;top:934px">
  <svg width="66" height="66" viewBox="0 0 64 64" fill="none" stroke="#22395f" stroke-width="2"><circle cx="32" cy="32" r="28"/><circle cx="32" cy="32" r="5" stroke="#0677BA"/><path d="M32 27c-2-8 2-16 8-15 4 2 2 10-4 16M37 32c8-2 16 2 15 8-2 4-10 2-16-4M32 37c2 8-2 16-8 15-4-2-2-10 4-16M27 32c-8 2-16-2-15-8 2-4 10-2 16 4"/></svg>
  <h3>Air Conditioning</h3><div class="bar"></div>
  <p>when an unknown printer took<br>a galley of type and scrambled<br>it to make a type specimen</p>
</article>
<article class="abs svc" style="left:460px;top:934px">
  <svg width="66" height="66" viewBox="0 0 64 64" fill="none" stroke="#22395f" stroke-width="2"><path d="M22 12c6 10 14 16 14 28a14 14 0 01-28 0c0-8 6-12 8-20 2 6 4 8 6 8z" stroke="#0677BA"/><rect x="44" y="6" width="8" height="40" rx="4"/><circle cx="48" cy="50" r="7"/><path d="M56 14h4M56 22h4M56 30h4"/></svg>
  <h3>Heating</h3><div class="bar"></div>
  <p>when an unknown printer took<br>a galley of type and scrambled<br>it to make a type specimen</p>
</article>
<article class="abs svc" style="left:805px;top:934px">
  <svg width="66" height="66" viewBox="0 0 64 64" fill="none" stroke="#22395f" stroke-width="2"><circle cx="36" cy="20" r="10" stroke="#0677BA"/><circle cx="36" cy="20" r="4" stroke="#0677BA"/><path d="M6 40h10v18H6zM16 44h14c4 0 6 4 2 6h-8M16 54h18l20-10c4-2 2-6-2-6l-12 4"/></svg>
  <h3>Maintenance</h3><div class="bar"></div>
  <p>when an unknown printer took<br>a galley of type and scrambled<br>it to make a type specimen</p>
</article>

<a class="abs pill" style="left:463px;top:1306px;width:272px;height:54px" href="#">BOOK A CONSULTATION</a>

<!-- WHAT WE TREAT -->
<div class="abs" style="left:20px;top:1380px;width:160px;height:200px;background:linear-gradient(180deg,#e7eef8,#c9d7ec);border-radius:6px" role="img" aria-label="Illustration of a technician installing a wall air conditioner"></div>
<div class="abs" style="left:1015px;top:1385px;width:150px;height:160px;background:linear-gradient(180deg,#e7eef8,#c9d7ec);border-radius:6px" role="img" aria-label="Illustration of a technician servicing an outdoor unit"></div>
<svg class="abs treat-bg" viewBox="0 0 1200 701" preserveAspectRatio="none">
  <defs><linearGradient id="tg" x1="0" y1="0" x2="0" y2="1"><stop offset="0" stop-color="#CADEEF"/><stop offset="1" stop-color="#E8F1F8"/></linearGradient></defs>
  <path d="M0 120 C250 40 420 20 600 60 C800 100 1000 10 1200 40 L1200 701 L0 701Z" fill="url(#tg)"/>
</svg>
<div class="abs art" style="left:113px;top:1625px;width:465px;height:398px;border:3px solid var(--brand);border-radius:6px;background:linear-gradient(135deg,#d9d4cc,#b9a89a 50%,#eae6e1)" role="img" aria-label="Photo of a smiling family relaxing at home"></div>
<h2 class="abs treat-title">WHAT <b>WE TREAT</b><span class="ln"></span></h2>
<p class="abs treat-copy">Lorem Ipsum is simply dummy text of the printing and typesetting industry. Lorem Ipsum has been the industry's standard dummy text ever since the 1500s,</p>
<ul class="abs treat-list" style="left:638px;top:1775px">
  <li>Air Conditioning</li><li>Heatinf</li><li>Heat Pumps/ Gas/Oil</li><li>Ductless Mini Splits</li><li>Controls</li>
</ul>
<ul class="abs treat-list" style="left:869px;top:1775px">
  <li>VFD's</li><li>Pumps</li><li>Gas Fitting</li><li>Service &amp; New Install</li><li>Residential / Commercial</li>
</ul>
<a class="abs pill" style="left:641px;top:1954px;width:189px;height:49px" href="#">ALL SERVICES</a>

<!-- TESTIMONIALS -->
<div class="abs underline" style="left:111px;top:2203px;width:52px"></div>
<h2 class="abs cl-title">WHAT <b>CLIENTS SAY</b></h2>
<div class="abs" style="left:500px;top:2233px;width:510px;height:1px;background:#dfe4ea"></div>
<svg class="abs" style="left:1035px;top:2225px" width="50" height="16" viewBox="0 0 50 16" fill="none" stroke-width="2"><path d="M18 8H2M8 2L2 8l6 6" stroke="#b9c4d3"/><path d="M30 8h16M40 2l6 6-6 6" stroke="#0054AA"/></svg>

<article class="abs review featured" style="left:113px">
  <div class="avatar" style="left:32px" role="img" aria-label="Client portrait"></div>
  Lorem Ipsum is simply dummy text of the printing and typesetting industry. Lorem Ipsum has been the industry's.
  <div class="who">Dana Merrow<small>Service technicion</small></div>
  <div class="stars">★★★★★</div>
</article>
<article class="abs review" style="left:446px">
  <div class="avatar" style="left:32px" role="img" aria-label="Client portrait"></div>
  Lorem Ipsum is simply dummy text of the printing and typesetting industry. Lorem Ipsum has been the industry's.
  <div class="who">Dana Merrow<small>Service technicion</small></div>
  <div class="stars">★★★★<i>★</i></div>
</article>
<article class="abs review" style="left:781px">
  <div class="avatar" style="left:32px" role="img" aria-label="Client portrait"></div>
  Lorem Ipsum is simply dummy text of the printing and typesetting industry. Lorem Ipsum has been the industry's.
  <div class="who">Dana Merrow<small>Service technicion</small></div>
  <div class="stars">★★★★<i>★</i></div>
</article>

<!-- CTA -->
<svg class="abs cta-bg" viewBox="0 0 1200 560" preserveAspectRatio="none">
  <defs><linearGradient id="cg" x1="0" y1="0" x2="1" y2="0"><stop offset="0" stop-color="#0054AA"/><stop offset="1" stop-color="#0a4fa0"/></linearGradient></defs>
  <path d="M0 0 H880 C1000 0 1060 60 1120 140 C1160 200 1200 230 1200 230 V560 H0Z" fill="url(#cg)"/>
</svg>
<div class="abs van-photo" role="img" aria-label="Photo of the company service van seen from the rear"></div>
<h2 class="abs cta-title">Top Rated Heating<br>and Air Conditioning<br>Service</h2>
<h3 class="abs cta-sub">Dedicated to Honesty and Trust</h3>
<p class="abs cta-copy">Contrary to popular belief, Lorem Ipsum is not simply random text. It has roots in a piece of classical Latin literature from 45 BC, making it over 2000 years old. Owen Hartley</p>
<a class="abs btn-white" style="left:109px;top:3087px;width:155px;height:47px" href="#">GET STARTED</a>
<a class="abs btn-line" style="left:282px;top:3087px;width:243px;height:47px" href="#">GET A FREE ESTIMATE ›</a>

<!-- ABOUT -->
<div class="abs underline" style="left:512px;top:3296px;width:52px"></div>
<h2 class="abs h-center about-title">ABOUT <b>US</b></h2>
<p class="abs h-center about-lead">Lorem Ipsum is simply dummy text of the printing and typesetting industry.</p>
<p class="abs about-copy">when an unknown printer took a galley of type and scrambled it to make a type specimen book. It has survived not only five centuries, but also the leap into electronic typesetting, remaining essentially unchanged. It was popularised in the 1960s with the release of Pressfold sheets containing Lorem Ipsum passages, and more recently with desktop publishing software like.</p>
<a class="abs pill" style="left:465px;top:3570px;width:273px;height:54px" href="#">BOOK A CONSULTATION</a>

<div class="abs banner" role="img" aria-label="Photo of a happy couple relaxing on a sofa"></div>
<h2 class="abs banner-text">Need To Get Your AC Repaired<br>or Replaced? Call Today!</h2>
<a class="abs btn-blue" style="left:874px;top:3783px;width:160px;height:44px" href="#">Get A Quote</a>

<!-- FOOTER -->
<footer class="abs footer"></footer>
<div class="abs" style="left:113px;top:4062px"><div class="brand"><span class="mark"></span>Quillfield HVAC</div></div>
<h2 class="abs f-quality">Quality Air<br>Conditioning Service</h2>

<h3 class="abs f-head" style="left:111px;top:4181px">Contact</h3>
<div class="abs" style="left:423px;top:4175px;width:1px;height:240px;background:#33507f"></div>
<div class="abs f-ic" style="left:111px;top:4238px"><svg width="26" height="20" viewBox="0 0 26 20" fill="none" stroke="#fff" stroke-width="1.8"><rect x="1" y="1" width="24" height="18" rx="2"/><path d="M1 3l12 9 12-9"/></svg></div>
<div class="abs f-text" style="left:185px;top:4242px">Email:<span>hello@quillfieldhvac.com</span></div>
<div class="abs f-ic" style="left:111px;top:4320px"><svg width="22" height="22" viewBox="0 0 24 24" fill="none" stroke="#fff" stroke-width="1.8"><path d="M6.6 10.8a15 15 0 006.6 6.6l2.2-2.2a1 1 0 011-.25 11.4 11.4 0 003.6.57 1 1 0 011 1V20a1 1 0 01-1 1A17 17 0 013 4a1 1 0 011-1h3.5a1 1 0 011 1c0 1.25.2 2.45.57 3.57a1 1 0 01-.25 1z"/></svg></div>
<div class="abs f-text" style="left:187px;top:4323px">Call Us:<span>555 014 2290</span></div>

<h3 class="abs f-head" style="left:509px;top:4181px">Links</h3>
<ul class="abs f-links" style="left:509px;top:4222px">
  <li>Home</li><li>About Us</li><li>Services</li><li>Blog</li><li>Sitemap</li><li>Location</li><li>Contact Us</li>
</ul>

<h3 class="abs f-head" style="left:754px;top:4181px">Our News Letter</h3>
<div class="abs f-input">Enter Your email....</div>
<div class="abs f-submit">SUBMIT<span class="ar"><svg width="12" height="14" viewBox="0 0 12 14"><path d="M3 1l6 6-6 6" stroke="#fff" stroke-width="2" fill="none"/></svg></span></div>

<div class="abs f-rule"></div>
<p class="abs f-bottom" style="left:111px">Copyright @ Quillfield 2024</p>
<p class="abs f-bottom" style="left:387px">Cookie policy &nbsp;| &nbsp;Terms of Condition</p>
<span class="abs social" style="left:977px"></span>
<span class="abs social" style="left:1016px"></span>
<span class="abs social" style="left:1053px"></span>

</body>
</html>
```